Services Brochure

We need an revised brochure for our 3 main services. I have uploaded our old Brochure for reference. We have 3 main services (Managed IT Services, Business VoIP, Business Internet). Below is some text we would like included in the brochure for each service section. In addition I have attached a "mock up" showing that we want IT Services on top, VoIP in the middle and Internet at the bottom. Please use your design experience to select images that would fit well. I also included an image of the phone we would like to use.
Text for Brochure:
Title/Header: Unleash the Power of Local IT Solutions
IT Services That Mean Business
Experience fanatical customer service with our affordable, full-service IT solutions. We’re 100% local, ensuring leading response times and personalized support—so you can focus on what you do best.
Talk More, Worry Less with Our Telephone Services
Say goodbye to overpriced equipment and hello to our free phone plan. Keep your number and enjoy unlimited local and long-distance calling. Tailor your phone system to your business needs and rest assured—our rates are always the lowest in town.
Highspeed Internet That Sets You Apart
Stay connected with blazing-fast speeds—from 1Gbps to 10Gbps, both up and down. Benefit from a static IP address and unbeatable prices, backed by 100% local support. Get the connectivity your business deserves at the best value in town.
Elevate your business with cutting-edge technology.
Sorry everyone the banner size is 81" high and 33" wide.

```html
<!DOCTYPE html>
<html lang="en">
<head>
<meta charset="utf-8">
<title>Nexa Services Flyer</title>
<link rel="stylesheet" href="https://fonts.googleapis.com/css2?family=Poppins:wght@600;700;800&family=Montserrat:wght@400;500&display=swap">
<style>
  :root {
    --navy: #28337b;
    --green: #8dc63f;
    --panel-green: #3fba4a;
    --lime: #b8e23a;
    --white: #ffffff;
    --backdrop: #727579;
    --device: #3a3f48;
  }
  * { margin: 0; padding: 0; box-sizing: border-box; }
  html, body { width: 1200px; height: 1200px; overflow: hidden; background: var(--backdrop); }
  .flyer {
    position: absolute; left: 243px; top: 100px;
    width: 714px; height: 1000px; background: var(--white); overflow: hidden;
    font-family: "Montserrat", sans-serif; color: var(--navy);
  }
  .shapes { position: absolute; inset: 0; }
  .brand {
    position: absolute; left: 97px; top: 26px;
    font-family: "Poppins", sans-serif; font-weight: 700; font-size: 76px;
    letter-spacing: -2px; color: var(--navy); line-height: 1;
  }
  .headline {
    position: absolute; left: 38px; top: 140px;
    font-family: "Poppins", sans-serif; font-weight: 800;
    font-size: 46px; line-height: 42px; letter-spacing: -1.5px; text-transform: uppercase;
  }
  .headline .navy { color: var(--navy); display: block; }
  .headline .lime { color: var(--green); display: block; }
  .product-shot {
    position: absolute; left: 303px; top: 90px; width: 354px; height: 262px;
    border-radius: 18px 18px 8px 30px;
    background: linear-gradient(160deg, #4a505b 0%, #2c3038 70%, #c9ccd1 100%);
  }
  .section-tab {
    position: absolute; left: 33px; top: 346px;
    font-family: "Poppins", sans-serif; font-weight: 700; font-size: 27px; color: var(--navy);
  }
  .service { position: absolute; left: 0; width: 410px; }
  .service .num {
    position: absolute; left: 32px; top: 0; width: 28px; height: 28px; border-radius: 50%;
    background: var(--green); color: var(--navy);
    font-family: "Poppins", sans-serif; font-weight: 700; font-size: 17px;
    display: flex; align-items: center; justify-content: center;
  }
  .service .rail {
    position: absolute; left: 45px; top: 34px; width: 0;
    border-left: 2px dotted var(--white);
  }
  .service h3 {
    position: absolute; left: 81px; top: 0; width: 320px;
    font-family: "Poppins", sans-serif; font-weight: 700; font-size: 17.5px;
    line-height: 26px; color: var(--green);
  }
  .service p {
    position: absolute; left: 81px; width: 312px;
    font-size: 12.6px; line-height: 16.8px; color: var(--white);
  }
  .photo {
    position: absolute; left: 443px; width: 238px; height: 152px;
    border: 1.5px solid var(--navy); border-radius: 0 16px 0 16px; overflow: hidden;
  }
  .photo::before {
    content: ""; position: absolute; left: 3px; top: 3px; width: 26px; height: 26px;
    background: var(--green); clip-path: polygon(0 0, 100% 0, 0 100%);
  }
  .photo-support { top: 403px; background: linear-gradient(135deg, #b9c6d2, #eef2f5 55%, #7f9bb5); }
  .photo-voip { top: 569px; background: linear-gradient(135deg, #0c1a44, #1f3f7a 55%, #0a1330); }
  .photo-internet { top: 737px; background: linear-gradient(110deg, #120c3a, #3a2a9a 45%, #4aa3e8 75%, #101a5a); }
  .call {
    position: absolute; left: 37px; top: 933px; display: flex; align-items: center; gap: 12px;
    font-family: "Poppins", sans-serif; color: var(--navy);
  }
  .call .label { font-weight: 700; font-size: 28px; }
  .call .number { font-weight: 800; font-size: 30px; letter-spacing: -0.3px; }
  .call svg { width: 28px; height: 28px; }
  .contacts { position: absolute; left: 475px; top: 928px; font-size: 16.5px; color: var(--navy); }
  .contacts li { list-style: none; display: flex; align-items: center; gap: 9px; height: 24px; }
  .contacts svg { width: 14px; height: 14px; }
</style>
</head>
<body>
<div class="flyer">
  <svg class="shapes" viewBox="0 0 714 1000" width="714" height="1000" aria-hidden="true">
    <defs>
      <radialGradient id="burst" cx="0.85" cy="0.25" r="0.8">
        <stop offset="0" stop-color="var(--lime)"/>
        <stop offset="0.45" stop-color="#5cc543"/>
        <stop offset="1" stop-color="var(--panel-green)"/>
      </radialGradient>
    </defs>
    <path d="M400 0 H714 V371 H430 Q400 371 400 341 Z" fill="url(#burst)"/>
    <path d="M0 342 H228 L269 386 H0 Z" fill="var(--green)"/>
    <path d="M0 386 V364 H371 Q380 364 386 372 L405 398 Q410 405 410 414 V905 L461 1000 H448 L402 915 H0 Z" fill="var(--navy)"/>
    <path d="M0 364 H240 L257 386 H0 Z" fill="var(--green)"/>
    <path d="M428 923 H714 V1000 H470 Z" fill="var(--green)"/>
  </svg>

  <div class="brand">nexa</div>

  <h1 class="headline">
    <span class="navy">Unleash</span>
    <span class="lime">The Power</span>
    <span class="navy">Of Local IT</span>
    <span class="lime">Solutions</span>
  </h1>

  <div class="product-shot" role="img" aria-label="Photo of a desk IP phone with handset and colour display"></div>

  <h2 class="section-tab">Our Services</h2>

  <section class="service" style="top:418px">
    <span class="num">1</span>
    <span class="rail" style="height:116px"></span>
    <h3>IT Services That Mean Business</h3>
    <p style="top:38px">Experience fanatical customer service with our affordable, full-service IT solutions. We’re 100% local, ensuring leading response times and personalized support—so you can focus on what you do best.</p>
  </section>

  <section class="service" style="top:563px">
    <span class="num">2</span>
    <span class="rail" style="height:130px"></span>
    <h3>Talk More, Worry Less with Our Telephone Services</h3>
    <p style="top:57px">Say goodbye to overpriced equipment and hello to our free phone plan. Keep your number and enjoy unlimited local and long-distance calling. Tailor your phone system to your business needs and rest assured—our rates are always the lowest in town.</p>
  </section>

  <section class="service" style="top:741px">
    <span class="num">3</span>
    <span class="rail" style="height:106px"></span>
    <h3>Highspeed Internet That Sets You Apart</h3>
    <p style="top:57px">Stay connected with blazing-fast speeds—from 1Gbps to 10Gbps, both up and down. Benefit from a static IP address and unbeatable prices, backed by 100% local support. Get the connectivity your business deserves at the best value in town.</p>
  </section>

  <div class="photo photo-support" role="img" aria-label="Photo of a smiling support agent with a headset in a bright office"></div>
  <div class="photo photo-voip" role="img" aria-label="Photo of a technician on a headset call in a server room"></div>
  <div class="photo photo-internet" role="img" aria-label="Abstract light trails suggesting high-speed data"></div>

  <div class="call">
    <span class="label">Call Us</span>
    <svg viewBox="0 0 28 28" aria-hidden="true">
      <circle cx="14" cy="14" r="14" fill="var(--green)"/>
      <path d="M10.2 7.5c.6-.3 1.2 0 1.5.5l1.3 2.3c.3.5.2 1.1-.3 1.5l-.9.7c.7 1.6 1.9 2.9 3.5 3.7l.7-.9c.4-.5 1-.6 1.5-.3l2.3 1.3c.5.3.8.9.5 1.5l-.6 1.3c-.4.8-1.3 1.2-2.2 1-4.6-1.1-8.1-4.7-9.2-9.3-.2-.9.2-1.8 1-2.2z" fill="var(--white)"/>
    </svg>
    <span class="number">555.014.2290</span>
  </div>

  <ul class="contacts">
    <li>
      <svg viewBox="0 0 14 14" aria-hidden="true"><g fill="none" stroke="var(--navy)" stroke-width="1.1"><circle cx="7" cy="7" r="6"/><ellipse cx="7" cy="7" rx="2.6" ry="6"/><path d="M1 7h12M2 4h10M2 10h10"/></g></svg>
      www.nexalocalit.com
    </li>
    <li>
      <svg viewBox="0 0 14 14" aria-hidden="true"><rect x="0.5" y="2.5" width="13" height="9" fill="var(--navy)"/><path d="M1 3l6 4.5L13 3" fill="none" stroke="var(--green)" stroke-width="1.1"/></svg>
      sales@nexalocalit.com
    </li>
  </ul>
</div>
</body>
</html>
```